Business Card and Stationary Design

After the successful redesign of our logo we are wanting to follow suite and create a new business card and stationary design!

New Logo is attached, information required on the business card should contain a mixture of the following but layout/arrangement is up to the designer.

Happy if the national provider number and abn are on the back, and happy for them to be smaller than the rest.

I am also happy to receive single sided or weird and wonderful designs.

Name
Title
National Provider Number 7291
ABN 53 219 864 317
Level 3, 42 Marlow Street
Carrowen NSW 2318
Ph: 1300 987 214
Mobile: 0432 785 619
name@ferngatebuild.com.au
www.ferngatebuild.com.au

Target Market(s)

Professionals, Peers, Students, Suppliers...

Industry/Entity Type

Construction

Contact Information for Business Card

Listed in project description

Font styles to use
Other font styles liked:
• Century Gothic

Colors
0455a3
3176b5
ffffff

Requirements
Must have
• Professional Design, same color scheme as our logo
Nice to have
• Something that sets our apart from everyone else would be fantastic, open to size and shape and layout options, as long as they present professionally.
• Open to raised/embossed text, alternative materials, custom sizes, clear material
Should not have
• The color orange

```html
<!DOCTYPE html>
<html lang="en">
<head>
<meta charset="utf-8">
<title>Ferngate Build – Business Card</title>
<link rel="stylesheet" href="https://fonts.googleapis.com/css2?family=Questrial&family=Montserrat:wght@700&display=swap">
<style>
  :root {
    --navy: #203877;
    --band: #2a77b8;
    --white: #ffffff;
    --ink: #111111;
    --backdrop: #e4e5e7;
  }
  html, body {
    margin: 0;
    width: 1200px;
    height: 1200px;
    overflow: hidden;
    background: var(--backdrop);
  }
  .card {
    position: absolute;
    left: 238px;
    top: 419px;
    width: 723px;
    height: 361px;
    background: var(--white);
    font-family: "Questrial", sans-serif;
    overflow: hidden;
  }
  .card__top {
    position: absolute;
    left: 0; top: 0;
    width: 100%;
    height: 207px;
    background: var(--navy);
    color: var(--white);
  }
  .card__band {
    position: absolute;
    left: 0; top: 207px;
    width: 100%;
    height: 16px;
    background: var(--band);
  }
  .contact {
    position: absolute;
    right: 28px;
    top: 28px;
    text-align: right;
  }
  .contact__name {
    font-size: 28px;
    line-height: 1;
    margin: 0;
    font-weight: 400;
  }
  .contact__name strong {
    font-family: "Montserrat", sans-serif;
    font-weight: 700;
  }
  .contact__title {
    font-size: 19px;
    margin: 4px 0 22px;
  }
  .contact__line {
    font-size: 20px;
    line-height: 24px;
    margin: 0;
    letter-spacing: 0.2px;
  }
  .contact__label {
    font-family: "Montserrat", sans-serif;
    font-weight: 700;
    font-size: 18px;
  }
  .details {
    position: absolute;
    left: 30px;
    top: 248px;
    color: var(--ink);
    font-size: 19.5px;
    line-height: 21.5px;
  }
  .details p { margin: 0; }
  .brand {
    position: absolute;
    right: 28px;
    top: 268px;
    display: flex;
    align-items: center;
    gap: 12px;
  }
  .brand__square {
    width: 26px;
    height: 26px;
    background: var(--navy);
  }
  .brand__name {
    font-size: 38px;
    line-height: 1;
    color: var(--navy);
    letter-spacing: 0.5px;
  }
</style>
</head>
<body>
  <div class="card">
    <section class="card__top">
      <div class="contact">
        <h1 class="contact__name"><strong>Na</strong> me</h1>
        <p class="contact__title">Title</p>
        <p class="contact__line"><span class="contact__label">P</span> | 1300 987 214</p>
        <p class="contact__line"><span class="contact__label">M</span> | 0432 785 619</p>
        <p class="contact__line">name@ferngatebuild.com.au</p>
        <p class="contact__line">www.ferngatebuild.com.au</p>
      </div>
    </section>
    <div class="card__band"></div>
    <section class="details">
      <p>National Provider Number 7291</p>
      <p>ABN 53 219 864 317</p>
      <p>Level 3, 42 Marlow Street</p>
      <p>Carrowen NSW 2318</p>
    </section>
    <div class="brand">
      <span class="brand__square"></span>
      <span class="brand__name">ferngate build</span>
    </div>
  </div>
</body>
</html>
```